create clean, simple business card template

using the logo created now we need to create a simple, elegant business card design to suit

Industry/Entity Type

Business

Font styles to use
Other font styles liked:
• segoe ui

Requirements
Must have
• Front:
"Name:"
"Title:"
"Mobile:"
"email:"
and the logo

Back:
Logo
Nice to have
• Text in black but other graphics etc to match colours in logo as provided

```html
<!DOCTYPE html>
<html lang="en">
<head>
<meta charset="utf-8">
<title>Kestrel Homes – Business Card</title>
<link rel="stylesheet" href="https://fonts.googleapis.com/css2?family=Open+Sans:ital,wght@0,400;0,600;0,700;1,400&display=swap">
<style>
  :root {
    --backdrop: #8f8f8f;
    --card: #ffffff;
    --ink: #111111;
    --forest: #2d342b;
    --gold: #917830;
  }
  * { box-sizing: border-box; margin: 0; padding: 0; }
  html, body {
    width: 1200px;
    height: 1000px;
    overflow: hidden;
    background: var(--backdrop);
    font-family: "Open Sans", "Segoe UI", sans-serif;
    color: var(--ink);
  }
  .canvas { position: relative; width: 1200px; height: 1000px; }
  .card {
    position: absolute;
    background: var(--card);
    overflow: hidden;
    box-shadow: 0 4px 10px rgba(0,0,0,0.35);
  }
  .card--front { left: 95px; top: 35px; width: 820px; height: 460px; }
  .card--back  { left: 305px; top: 520px; width: 800px; height: 445px; }

  .holder { position: absolute; right: 115px; top: 50px; text-align: right; }
  .holder__name { font-size: 31px; font-weight: 700; line-height: 1.1; }
  .holder__title { font-size: 20px; font-style: italic; margin-top: 2px; }

  .contact { position: absolute; left: 235px; top: 170px; font-size: 20px; white-space: nowrap; }
  .contact span + span { margin-left: 14px; }

  .brand { position: absolute; display: flex; align-items: center; gap: 14px; }
  .brand__dot { width: 22px; height: 22px; border-radius: 50%; background: var(--forest); flex: none; }
  .brand__name { font-weight: 600; color: var(--gold); white-space: nowrap; }
  .card--front .brand { left: 285px; top: 330px; }
  .card--front .brand__name { font-size: 40px; }
  .card--back .brand { left: 50%; top: 130px; transform: translateX(-50%); }
  .card--back .brand__name { font-size: 50px; }

  .band { position: absolute; bottom: 0; }
  .band--forest { left: 0; width: 430px; height: 45px; background: var(--forest); }
  .band--gold { left: 430px; right: 0; height: 70px; background: var(--gold); }

  .skyline {
    position: absolute; left: 0; right: 0; bottom: 0; height: 130px;
    background: linear-gradient(to top, var(--forest) 75%, #3a4238 100%);
  }
</style>
</head>
<body>
<main class="canvas">
  <section class="card card--front" aria-label="Business card front">
    <div class="holder">
      <p class="holder__name">Anselm Whitby</p>
      <p class="holder__title">Director</p>
    </div>
    <p class="contact"><span>T: +91 9845120467</span><span>E: hello@kestrelhomes.org</span></p>
    <div class="brand">
      <span class="brand__dot"></span>
      <span class="brand__name">Kestrel Homes</span>
    </div>
    <div class="band band--forest"></div>
    <div class="band band--gold"></div>
  </section>

  <section class="card card--back" aria-label="Business card back">
    <div class="brand">
      <span class="brand__dot"></span>
      <span class="brand__name">Kestrel Homes</span>
    </div>
    <div class="skyline" role="img" aria-label="Dark silhouette of a city skyline with tall towers"></div>
  </section>
</main>
</body>
</html>
```